Webdesign für Industrieanlagenbau-Unternehmen
Zielgruppe
Die ZEV services GmbH ist ein ein österreichisches, eigentümergeführtes Industrieanlagenbau-Unternehmen mit Niederlassungen an derzeit 2 Standorten (Brunnstetten/NÖ und Almreith/Sbg) und ist in den Geschäftsfeldern Industrieanlagenbau, Reinraumtechnik und Sondermaschinenbau - sowie im Projekt- und Behördenmanagement tätig.
Die ZEV services GmbH unterstützt ihre B2B-Kunden bei der Umsetzung von Engineering-Projekten in der Hightech-, Elektronik- und Prozessindustrie.
Unsere Kernkompetenzen sind Konzepterstellung, 3D-Planung, Konstruktion, Design und Montage von Prozessanlagen und Reinräumen, eine eigene Fertigung und Prototypenbau in unserer „Metall-& Kunststoff Manufaktur“ sowie die Abwicklung des Behörden-Managements wie z.B. Einreichverfahren nach Gewerbeordnung.
Langjährige und dauerhafte Geschäftsbeziehungen zu unseren Kunden stehen bei uns im Vordergrund.
Zielsgruppe der neuen website:
„Visitenkarte“ der ZEV services GmbH
potentielle Mitarbeiter („Employer Branding“), Ingenieure/Projektmanager (WI-Maschinenbau, Elektro- und Prozesstechnik), Mechatroniker, Schlosser, Elektriker
B2B Kunden aus Bereichen Mikroelektronik-Fertigung, chemische Industrie, Lebensmittel- und Pharmaproduktion
Bestandskunden (Stakeholder des „Buying Centers“ bei Kunden)
Neukunden „eingeschränkt“ (dzt. Keine aktive Kundenakquise via web geplant)
Aufgabenstellung
Allgemeine Anforderungen an die neue website:
Ziel sind eher „schlanke“ Texte & Design (vgl. https://www.valdrin-gruppe.com/de/)
Produkt- und Leistungsspezifisches Bildmaterial sollen hauptsächlich ZEV-eigene Fotos und Videos sein (Stock-Fotos nur für Allgemeine Bilder). Beispielhaftes Bildmaterial (sollte durch ZEV Mitarbeiter dann im CMS einfach ausgetauscht werden können) in diesen Unterlagen
CMS (Content Management System) zur Administration durch ZEV Mitarbeiter
Hosting auf europäischen ServernServern (z.B. https://voll-pack.com/, https://www.brommlat.com, https://www.kessfurt.de, https://www.ornix2go.com/, https://www.puvo.at)
Basierend auf weitverbreiteten open-Source Systemen (z.B. Wordpress , Joomla, TYPO3)
Responsive Webdesign – eine Website für alle Geräte (PC, Tablet, Smartphone) und alle gängigen Browser (Chrome, Edge, Safari, Firefox, Opera, Internet Explorer)
Google Pagespeed mind. 85 Punkte, GTmetrix Grade > 80%
Sicherheitszertifikat (SSL-Zertifikat)
Sprache – Deutsch, Englisch
E-Commerce-Gesetz (ECG) & DSGVO konform (Cookie Disclaimer Standard „nur notwendige“)
Impressum
AGB - Allgemeine Lieferungs- und Zahlungsbedingungen
Sitemap
Vollständige Rechte an der website (Design, Inhalt etc.) bei ZEV services GmbH
Einbettung von Text, Fotos und Videos durch ZEV Mitarbeiter
Hinzufügen von Menü-Unterpunkten durch ZEV Mitarbeiter

```html
<!DOCTYPE html>
<html lang="de">
<head>
<meta charset="utf-8">
<title>ZEV services GmbH – Leistungen</title>
<link href="https://fonts.googleapis.com/css2?family=Open+Sans:wght@400;600;700&display=swap" rel="stylesheet">
<style>
:root{
  --red:#d7191f;
  --text:#444;
  --dark:#222;
  --bg:#f5f5f5;
  --band:#ececec;
  --footer:#0f1d2c;
  --dot:#c9c9c9;
  --footer-text:#e6e9ee;
}
*{box-sizing:border-box;margin:0;padding:0}
html,body{width:1200px;height:4417px;overflow:hidden}
body{font-family:"Open Sans",sans-serif;background:var(--bg);color:var(--text);position:relative}
.abs{position:absolute}
.header{left:0;top:0;width:1200px;height:130px;background:#fff}
.logo{display:flex;align-items:center;gap:10px;color:var(--red);font-weight:700;font-size:42px;letter-spacing:1px}
.logo .mark{width:30px;height:30px;background:var(--red)}
.nav a{position:absolute;top:55px;font-size:17px;font-weight:600;color:#333;text-decoration:none}
.nav a.active{color:var(--red)}
.hero{left:0;top:130px;width:1200px;height:320px;background:linear-gradient(90deg,#4a5466,#6a7890 45%,#55637a);display:flex;align-items:center;justify-content:center}
.hero h1{color:#fff;font-size:60px;font-weight:600}
.media{background:linear-gradient(135deg,#d9dde2,#9aa3ad)}
.media.white{background:#fff}
.arrow{position:absolute;top:50%;transform:translateY(-50%);width:24px;height:40px}
.arrow.l{left:12px}.arrow.r{right:12px}
.dots{display:flex;gap:6px}
.dots span{width:11px;height:11px;border-radius:50%;background:var(--dot)}
.dots span:first-child{background:var(--red)}
h2{color:var(--red);font-size:24px;font-weight:700;line-height:1.2;margin-bottom:12px}
p{font-size:15px;line-height:1.62}
.label{font-weight:700;color:#333;font-size:15px;margin:18px 0 8px}
.ticks{list-style:none}
.ticks li{position:relative;padding-left:31px;font-size:15px;line-height:1.4;margin-bottom:8px}
.ticks li svg{position:absolute;left:0;top:1px;width:20px;height:18px}
.band{left:0;top:2715px;width:1200px;height:557px;background:var(--band)}
.band h3{position:absolute;left:0;width:1200px;top:62px;text-align:center;color:var(--red);font-size:28px;font-weight:600}
.tabs a{position:absolute;top:115px;font-size:15.5px;color:#444;text-decoration:none}
.tabs a.active{font-weight:700;color:#333}
.footer{left:0;top:4080px;width:1200px;height:337px;background:var(--footer);color:var(--footer-text)}
.fcol{position:absolute;top:48px;font-size:14px;line-height:1.55}
.fcol h4{color:var(--red);font-size:16px;font-weight:600;margin-bottom:8px}
.footer .logo{color:#fff;font-size:40px}
.footer .logo .mark{background:#fff}
.addr{font-size:12.5px;line-height:1.55}
.addr b{font-weight:700}
.legal{position:absolute;top:302px;left:75px;font-size:11px;display:flex}
.legal a{color:var(--footer-text);margin-left:45px;text-decoration:underline}
</style>
</head>
<body>
<svg width="0" height="0" style="position:absolute">
  <defs>
    <symbol id="tick" viewBox="0 0 20 18"><path d="M2 9 L8 15 L18 2" fill="none" stroke="#d7191f" stroke-width="3.5" stroke-linecap="round" stroke-linejoin="round"/></symbol>
    <symbol id="chev-l" viewBox="0 0 24 40"><path d="M20 3 L4 20 L20 37" fill="none" stroke="currentColor" stroke-width="3"/></symbol>
    <symbol id="chev-r" viewBox="0 0 24 40"><path d="M4 3 L20 20 L4 37" fill="none" stroke="currentColor" stroke-width="3"/></symbol>
  </defs>
</svg>

<header class="abs header">
  <div class="abs logo" style="left:75px;top:42px"><span class="mark"></span>ZEV</div>
  <nav class="nav">
    <a style="left:470px">Home</a>
    <a class="active" style="left:570px">Leistungen</a>
    <a style="left:715px">Jobs/Karriere</a>
    <a style="left:880px">Kontakt</a>
    <a style="left:998px">Kunden-Portal</a>
  </nav>
</header>

<section class="abs hero" role="img" aria-label="Foto: Mitarbeiter in einer Maschinenhalle mit Turbinenanlage">
  <h1>Leistungen</h1>
</section>

<div class="abs media white" style="left:75px;top:513px;width:517px;height:406px;color:var(--red)">
  <div class="abs" role="img" aria-label="3D-Planung einer Industrieanlage" style="left:28px;top:130px;width:460px;height:150px;background:linear-gradient(90deg,#b9c0c8,#d5d9de 50%,#9fa9b4)"></div>
  <svg class="arrow l"><use href="#chev-l"/></svg><svg class="arrow r"><use href="#chev-r"/></svg>
</div>
<div class="abs dots" style="left:302px;top:936px"><span></span><span></span><span></span><span></span></div>
<div class="abs" style="left:648px;top:548px;width:420px">
  <h2>Industrieanlagenbau</h2>
  <p>In enger Zusammenarbeit mit Ihnen übernimmt ZEV services GmbH als Komplettanbiete den Neubau oder Modernisierung Ihrer Prozessanlagen.</p>
  <div class="label">Unser Portfolio:</div>
  <ul class="ticks">
    <li><svg><use href="#tick"/></svg>Konzepterstellung &amp; Design</li>
    <li><svg><use href="#tick"/></svg>Engineering &amp; 3D-Detailplanung</li>
    <li><svg><use href="#tick"/></svg>Automatisierung</li>
    <li><svg><use href="#tick"/></svg>Montage &amp; Inbetriebnahme</li>
    <li><svg><use href="#tick"/></svg>CE-Kennzeichnung</li>
    <li><svg><use href="#tick"/></svg>Behörden-Management und Einreichverfahren</li>
  </ul>
</div>

<div class="abs" style="left:122px;top:1163px;width:420px">
  <h2>Reinraumtechnik</h2>
  <p>Neben der Auslegung der Systeme zur Luftaufbereitung und -förderung planen wir gemeinsam mit Ihnen alle Funktionselemente und Komponenten wie Reinraum­wände, -decken und -böden. Unsere Leistung umfasst Konzepterstellung, Prozess- und Detailplanung.</p>
</div>
<div class="abs media" role="img" aria-label="Foto: Reinraumanlage in einer Fertigungshalle" style="left:608px;top:1061px;width:517px;height:406px;background:linear-gradient(180deg,#8da6c8,#c9ced5 45%,#a9aeb4);color:#fff">
  <svg class="arrow l"><use href="#chev-l"/></svg><svg class="arrow r"><use href="#chev-r"/></svg>
</div>
<div class="abs dots" style="left:834px;top:1484px"><span></span><span></span><span></span><span></span></div>

<div class="abs media" role="img" aria-label="Foto: Abfüllanlage aus Edelstahl" style="left:75px;top:1608px;width:517px;height:406px;background:linear-gradient(180deg,#c8ccd1,#8f969e 60%,#6e747a);color:#fff">
  <svg class="arrow l"><use href="#chev-l"/></svg><svg class="arrow r"><use href="#chev-r"/></svg>
</div>
<div class="abs dots" style="left:302px;top:2031px"><span></span><span></span><span></span><span></span></div>
<div class="abs" style="left:648px;top:1661px;width:440px">
  <h2>Sondermaschinenbau</h2>
  <p>Neben kundenindividuellen Lösungen und Assemblierung von Komponenten konstruieren wir unter anderem Abfüll- und Mischanlagen für verschiedene Industriezweige. Für den Rohrleitungsbau von Primär- &amp; Sekundärkühlkreislauf haben wir die Konstruktion &amp; 3D-Planung im Haus.</p>
  <p style="margin-top:24px">Wir planen, fertigen und montieren die Infrastruktur für Rack-Lösungen (Gerätebühnen, Zwischenböden, Podeste, usw.) und Löschsysteme für IT-Räume/Racks (gasförmige Löschmittel).</p>
</div>

<div class="abs" style="left:122px;top:2250px;width:390px">
  <h2>Gasversorgungsanlagen</h2>
  <p>Planung und Konstruktion von industriellen Abfüllanlagen für Versandbehälter, Zentralen Gaseversorgungsanlagen (ZGVs) inklusive Analytik und Gaswarnanlagen.</p>
</div>
<div class="abs media" role="img" aria-label="Foto: Gasflaschen und Rohrleitungen einer Gasversorgungsanlage" style="left:608px;top:2156px;width:517px;height:406px;background:linear-gradient(135deg,#a5acb4,#5f6f84 55%,#3d5370);color:#fff">
  <svg class="arrow l"><use href="#chev-l"/></svg><svg class="arrow r"><use href="#chev-r"/></svg>
</div>
<div class="abs dots" style="left:834px;top:2579px"><span></span><span></span><span></span><span></span></div>

<section class="abs band">
  <h3>Unsere Produkte</h3>
  <div class="tabs">
    <a class="active" style="left:227px">Materialschleusen für Reinräume</a>
    <a style="left:546px">Heizungs- &amp; Kälteverteiler</a>
    <a style="left:794px">Wärmetauscher-Station</a>
  </div>
  <svg class="abs" style="left:64px;top:290px;width:24px;height:40px;color:var(--red)"><use href="#chev-l"/></svg>
  <svg class="abs" style="left:1110px;top:290px;width:24px;height:40px;color:var(--red)"><use href="#chev-r"/></svg>
  <div class="abs" role="img" aria-label="Foto: Wärmetauscher-Station mit isolierten Rohrleitungen" style="left:146px;top:178px;width:390px;height:292px;background:linear-gradient(135deg,#c9ced3,#8f989f 55%,#6c7268)"></div>
  <p class="abs" style="left:557px;top:232px;width:470px">Durch ein Wärmetauscher-System wird der Sekundärkreislauf (zu den zu kühlenden bzw. zu wärmenden Anlagen) vom Primärkreislauf (Hauptkühl- bzw. -wärmekreislauf) getrennt. Die kompakte Bauweise und hocheffiziente Komponenten der ZEV WärmetauscherStation garantiert dauerhaft stabile Durchfluss und Temperaturprofile im Primärkreislauf der zu kühlenden bzw. wärmenden Anlagen. Die kundenspezifische Fertigung erfolgt an unserem Standort in Brunnstetten/NÖ.</p>
</section>

<div class="abs" style="left:122px;top:3432px;width:420px">
  <h2>Projekt-Management und<br>Behörden-Management</h2>
  <p>Mit unserem erfahrenen Engineering Team unterstützen wir Sie beim effizienten, sinnvollen und wirtschaftlichen Umgang mit Ihren Ressourcen.</p>
  <div class="label">Unsere Leistungen umfassen unter anderem:</div>
  <ul class="ticks">
    <li><svg><use href="#tick"/></svg>Behördenmanagement<br>(Gewerbebehördliche Genehmigung)</li>
    <li><svg><use href="#tick"/></svg>Konformitätsbewertung (CE)</li>
    <li><svg><use href="#tick"/></svg>Baustellenkoordination</li>
    <li><svg><use href="#tick"/></svg>Explosionsschutz</li>
    <li><svg><use href="#tick"/></svg>Dokumentation Arbeitnehmerschutz</li>
    <li><svg><use href="#tick"/></svg>Technische Dokumentation</li>
    <li><svg><use href="#tick"/></svg>Training / Unterweisung</li>
    <li><svg><use href="#tick"/></svg>Inbetriebnahme &amp; Übergabe</li>
  </ul>
</div>
<div class="abs" role="img" aria-label="Foto: Zwei Mitarbeiter besprechen ein Projekt am Tablet" style="left:608px;top:3432px;width:517px;height:406px;background:linear-gradient(135deg,#e4e6e9,#b9bec5 50%,#5b6069)"></div>

<footer class="abs footer">
  <div class="fcol" style="left:75px"><h4>Home</h4>Über ZEV<br>Kunden<br>Mission<br>Team</div>
  <div class="fcol" style="left:215px"><h4>Leistungen</h4>Industrieanlagenbau<br>Reinraumtechnik<br>Gasversorgungsanlagen<br>Sondermaschinenbau<br>Produkte<br>Projekt-Management<br>Behörden-Management</div>
  <div class="fcol" style="left:440px"><h4>Jobs &amp; Karriere</h4>Stellenangebote<br>Arbeiten bei ZEV</div>
  <div class="fcol" style="left:635px"><h4>Kundenportal</h4>Link zu NAS</div>
  <div class="abs logo" style="left:918px;top:42px"><span class="mark"></span>ZEV</div>
  <div class="abs addr" style="left:924px;top:106px">
    <b>Standort Almreith</b><br>Talgrundweg 12<br>A-5470 Almreith<br>Telefon: +43 (0) 500000-0
    <br><br><b>Standort Brunnstetten</b><br>Lindenhofgasse 8<br>A-2530 Brunnstetten<br>Telefon: +43 (0) 500000-0
  </div>
  <div class="legal"><span>© ZEV services GmbH 2021</span><a>Impressum</a><a>AGB</a><a>Datenschutz</a><a>Nachhaltigkeit</a></div>
</footer>
</body>
</html>
```